Großartige Zusammenarbeit. Schnell und absolut zuverlässig. Tolle eigene Idee eingebracht. Trelgrafik hat sich sehr mit dem Projekt beschäftigt und hat den Kern perfekt umgesetzt - besser geht nicht!
Zielgruppe
Wir sind der Lindmoorer Kai Verein. Ein Verein der sich für die Neugestaltung des historischen Hafens in Hamburg-Bergedorf stark macht und Projekte auch in die Tat umsetzt für Bergedorf. Finanziert werden wir durch unsere Mitglieder. Unsere Zielgruppe sind Bergedorfer - Privatleute / Firmen / Einzelhandel in Bergedorf. Menschen die Stolz auf Bergedorf sind und ein Teil dieses Prozessen sein möchten und aktiv Ideen haben, wie man das Hafenareal attraktiver gestalten kann.
Aufgabenstellung
Das Plakat-Projekt, welches es umzusetzen gilt, ist eine Veranstaltung die jährlich stattfindet in dem Kolmwik-Hafen. Der Kolmwik ist der Name des Gewässers. 2017 hat sie bereits stattgefunden. Wir brauchen mehr öffentliche Aufmerksamkeit, wollen hiermit potentielle Mitglieder ansprechen. Das Plakat wird z. B. in dem Markt Galerie Lindmoor aushängen, eventuell auch als digitale Werbung auf den Monitoren im Center geschaltet werden.
Zur Veranstaltung: Es gibt 4 Abende, jeweils spielt eine Live-Band (Rock / Blues / etc.) auf dem Deck eines Bootes der Lindmoorer Fährgesellschaft Musik. Vom Anleger aus verfolgen die Gäste das Event und Getränke gibt es auf dem Boot. Es ist ein Open Air Event. Bilder vom letzten Jahr gibt es auf der Webseite www.lindmoorer-kai.de/Aktuelles
Titel: Klang am Lindmoorer Kai
Text: Unter freiem Himmel als Schwimmbühne im Kolmwik. Bei Schlechtwetter in der Tonkeller im Wendthof
Zusatz: Live und umsonst / Bierverkauf vom Schiff
Textänderungen / weitere Vorschläge sind herzlich willkommen, Hauptsache es gibt einen Bezug zum Hafen und zu Bergedorf.
Hochformat: A2 und Flyer Format z.B. A6 / Übliche digitale Formate JPG / EPS / AI... und MP4 (1080x1920 Pixel 72 DPI)
Inhaltstext zu den Bands die spielen werden:
28.06.2018 / 19 Uhr Velvet Hornets (Blues Rock)
26.07.2018 / 19 Uhr Rusty Pistons ( Rock´n Roll)
30.08.2018 / 19 Uhr The Moorland Pipers ( Schottischer Highland Beat)
27.09.2018 / 19 Uhr Korvidan (Deutscher Rock)

```html
<!DOCTYPE html>
<html lang="de">
<head>
<meta charset="utf-8">
<title>Music on Kolmwik – Der Hafen rockt</title>
<link rel="stylesheet" href="https://fonts.googleapis.com/css2?family=Amatic+SC:wght@700&family=Baloo+2:wght@600;700&family=Montserrat:wght@300;700&display=swap">
<style>
  :root {
    --sky-top: #a6cbe0;
    --sky-mid: #c7d1d2;
    --water-mid: #6f8ea6;
    --water-deep: #243f5c;
    --accent: #f7ad3a;
    --white: #ffffff;
    --ink: #0f1c2b;
    --keys-light: #eef0f1;
    --keys-dark: #1a2733;
  }
  * { margin: 0; padding: 0; box-sizing: border-box; }
  html, body { width: 861px; height: 1200px; overflow: hidden; background: var(--white); }
  .poster {
    position: relative; width: 861px; height: 1200px; overflow: hidden;
    background: linear-gradient(180deg, var(--sky-top) 0%, var(--sky-mid) 36%, var(--water-mid) 62%, var(--water-deep) 100%);
    font-family: "Baloo 2", sans-serif; color: var(--white);
  }
  .piano-keys {
    position: absolute; left: 0; top: 0; width: 300px; height: 1200px;
    background: linear-gradient(90deg, var(--keys-dark) 0%, #5a6670 35%, var(--keys-light) 60%, var(--keys-light) 100%);
  }
  .title-word {
    position: absolute; font-family: "Amatic SC", sans-serif; font-weight: 700; line-height: 1;
  }
  .title-m { left: 282px; top: 88px; font-size: 200px; color: var(--accent); }
  .title-u { left: 462px; top: 196px; font-size: 120px; color: var(--accent); }
  .title-s { left: 520px; top: 80px; font-size: 160px; color: var(--white); font-family: "Montserrat", sans-serif; }
  .title-i { left: 632px; top: 86px; font-size: 150px; color: var(--white); }
  .title-c { left: 672px; top: 84px; font-size: 168px; color: var(--white); }
  .title-on { left: 356px; top: 276px; font-size: 58px; color: var(--white); }
  .title-place { left: 548px; top: 276px; font-size: 58px; color: var(--white); letter-spacing: 1px; }
  .headline {
    position: absolute; left: 330px; width: 480px; top: 378px; text-align: center;
    font-family: "Montserrat", sans-serif; font-weight: 700; font-size: 35px; letter-spacing: .5px;
  }
  .tagline {
    position: absolute; left: 330px; width: 480px; top: 596px; text-align: center;
    font-family: "Montserrat", sans-serif; font-weight: 300; font-size: 30px;
  }
  .concerts { position: absolute; left: 372px; width: 400px; top: 664px; text-align: center; list-style: none; }
  .concert { height: 127px; }
  .concert-date { font-size: 24px; font-weight: 700; line-height: 1.3; }
  .concert-band { font-size: 25px; font-weight: 700; color: var(--accent); line-height: 1.3; }
  .concert-genre { font-size: 17px; font-weight: 600; line-height: 1.6; }
  .weather-note {
    position: absolute; left: 813px; top: 1118px; transform: rotate(-90deg); transform-origin: left top;
    font-family: "Montserrat", sans-serif; font-size: 11.5px; white-space: nowrap;
  }
  .club {
    position: absolute; left: 44px; top: 994px; width: 290px; height: 102px;
    background: var(--white); display: flex; align-items: center; gap: 10px; padding: 0 14px;
  }
  .club-mark { width: 16px; height: 16px; background: var(--ink); flex: none; }
  .club-name { font-size: 23px; font-weight: 600; color: var(--ink); }
</style>
</head>
<body>
<main class="poster">
  <div class="piano-keys" role="img" aria-label="Illustration: schräg versetzte Klaviertasten in Schwarz und Weiß mit Grunge-Struktur"></div>

  <h1 aria-label="Music on Kolmwik">
    <span class="title-word title-m">M</span>
    <span class="title-word title-u">U</span>
    <span class="title-word title-s">S</span>
    <span class="title-word title-i">I</span>
    <span class="title-word title-c">C</span>
    <span class="title-word title-on">ON</span>
    <span class="title-word title-place">KOLMWIK</span>
  </h1>

  <p class="headline">DER HAFEN ROCKT</p>
  <p class="tagline">LIVE UND UMSONST</p>

  <ul class="concerts">
    <li class="concert">
      <div class="concert-date">28.06.2018</div>
      <div class="concert-band">19 Uhr Velvet Hornets</div>
      <div class="concert-genre">(Blues Rock)</div>
    </li>
    <li class="concert">
      <div class="concert-date">26.07.2018</div>
      <div class="concert-band">19 Uhr Rusty Pistons</div>
      <div class="concert-genre">(Rock´n Roll)</div>
    </li>
    <li class="concert">
      <div class="concert-date">30.08.2018</div>
      <div class="concert-band">19 Uhr The Moorland Pipers</div>
      <div class="concert-genre">(Schottischer Highland Beat)</div>
    </li>
    <li class="concert">
      <div class="concert-date">27.09.2018</div>
      <div class="concert-band">19 Uhr Korvidan</div>
      <div class="concert-genre">(Deutscher Rock)</div>
    </li>
  </ul>

  <p class="weather-note">Bei Schlechtwetter finden die Konzerte in der Tonkeller im Wendthof statt.</p>

  <div class="club">
    <span class="club-mark"></span>
    <span class="club-name">Lindmoorer Kai Verein</span>
  </div>
</main>
</body>
</html>
```